Sales Page Header Design Project

Hi,
I need a background image created for this sales page: http://tidyventurecamp.example
Width: 977 px
Height: 150 px
Here are a few sample designs to work with: http://marketsummitschool.example/
http://crafthousepixel.example/wp-content/uploads/2011/02/experts1.png
Must be sharp, professional looking and uncluttered.
Colours: Must include blue (I like the blue on the on the current sales page, but will leave shade and colour combinations to your creativity)
Text = Tunde Marwick Presents
Tidy Venture Camp
Your Blueprint for Building a Profitable, Sustainable Business in Today's Economy!
Any questions, give me a shout
Entrepreneurs and Business Owners, aged 21 to 45
Business

```html
<!DOCTYPE html>
<html lang="en">
<head>
<meta charset="utf-8">
<title>Tunde Marwick Presents – Tidy Venture Camp</title>
<link rel="stylesheet" href="https://fonts.googleapis.com/css2?family=Ubuntu:wght@500;700&display=swap">
<style>
  :root {
    --sky: #2ecdf4;
    --sky-deep: #22b9e6;
    --grid-line: rgba(255, 255, 255, 0.28);
    --cloud: #f4f6f8;
    --navy: #1b1670;
    --link-blue: #1f6cc2;
    --violet: #45309a;
  }
  html, body {
    margin: 0;
    padding: 0;
    overflow: hidden;
    background: #ffffff;
  }
  .header-banner {
    position: relative;
    width: 1200px;
    height: 184px;
    overflow: hidden;
    background: radial-gradient(ellipse at 50% 50%, var(--sky) 60%, var(--sky-deep) 100%);
    font-family: "Ubuntu", sans-serif;
  }
  .backdrop {
    position: absolute;
    inset: 0;
  }
  .headline {
    position: absolute;
    left: 0;
    right: 0;
    margin: 0;
    text-align: center;
  }
  .presenter {
    top: 6px;
    font-size: 36px;
    font-weight: 500;
    color: var(--navy);
    letter-spacing: 0.2px;
  }
  .programme {
    top: 49px;
    font-size: 19px;
    font-weight: 500;
    color: var(--link-blue);
  }
  .tagline {
    top: 133px;
    font-size: 24px;
    font-weight: 500;
    color: var(--violet);
  }
</style>
</head>
<body>
  <header class="header-banner">
    <svg class="backdrop" width="1200" height="184" viewBox="0 0 1200 184" aria-hidden="true">
      <defs>
        <pattern id="blueprint-grid" width="25" height="25" patternUnits="userSpaceOnUse">
          <path d="M25 0H0V25" fill="none" stroke="var(--grid-line)" stroke-width="1.2"/>
        </pattern>
      </defs>
      <rect width="1200" height="184" fill="url(#blueprint-grid)"/>
      <g class="clouds" fill="var(--cloud)">
        <ellipse cx="68" cy="10" rx="50" ry="44"/>
        <ellipse cx="228" cy="12" rx="18" ry="25"/>
        <ellipse cx="22" cy="156" rx="52" ry="38"/>
        <ellipse cx="994" cy="10" rx="44" ry="44"/>
        <ellipse cx="1126" cy="78" rx="80" ry="104"/>
        <ellipse cx="1112" cy="190" rx="30" ry="22"/>
      </g>
    </svg>
    <h1 class="headline presenter">Tunde Marwick Presents</h1>
    <h2 class="headline programme">Tidy Venture Camp</h2>
    <p class="headline tagline">Your Blueprint for Building a Profitable, Sustainable Business in Today’s Economy!</p>
  </header>
</body>
</html>
```